Truck Parking Fyer Design

We need a flyer design for a new company based in Redland Bay called "Wattle Downs Truck Parking"
We have parking available for Tipper Trucks, Earthmoving Machinery & Shipping containers. Undercover area for Cars, Motorhomes, Caravans, Horse Floats and Boats. Rates are negotiable on length of time needed. eg. Truck and Dog = $50 per week + GST. 20 foot container $25 per week. Idea for local Redlands Residents. Owners are responsible for own insurance. We would like to see it as a simple design including different types of vehicles as mentioned above. with colours of earthmoving green (like grass) and brown like (dirt) - Lockup parking with owners living on site

```html
<!DOCTYPE html>
<html lang="en">
<head>
<meta charset="utf-8">
<title>Wattle Downs Truck Parking</title>
<link href="https://fonts.googleapis.com/css2?family=Russo+One&family=Roboto+Condensed:wght@400;700&family=Oswald:wght@400;500;600&display=swap" rel="stylesheet">
<style>
  :root {
    --grass: #8cc43c;
    --dirt: #4a2a14;
    --dirt-light: #6b3f1f;
    --red: #d7262a;
    --green-text: #5c9a2a;
    --ink: #1f1a16;
    --white: #ffffff;
    --badge-yellow: #f2e233;
  }
  html, body { margin: 0; padding: 0; overflow: hidden; background: #ffffff; }
  .flyer {
    position: relative;
    width: 907px;
    height: 1200px;
    overflow: hidden;
    background: #ffffff;
    font-family: "Roboto Condensed", "Arial Narrow", sans-serif;
  }
  .backdrop { position: absolute; inset: 0; }
  .business-name {
    position: absolute; left: 0; right: 0; top: 48px; margin: 0;
    text-align: center;
    font-family: "Oswald", sans-serif; font-weight: 500; font-size: 46px;
    letter-spacing: 1px; color: var(--dirt); text-transform: uppercase;
  }
  .headline {
    position: absolute; left: 0; right: 0; top: 156px; margin: 0;
    text-align: center; font-family: "Russo One", sans-serif;
    font-size: 60px; line-height: 66px; color: var(--white); font-weight: 400;
    text-shadow: 0 3px 4px rgba(0,0,0,0.35);
  }
  .offer-pill {
    position: absolute; left: 307px; top: 322px; width: 291px; height: 56px;
    border-radius: 28px;
    background: linear-gradient(var(--dirt-light), var(--dirt));
    box-shadow: 0 4px 6px rgba(0,0,0,0.35);
    color: var(--white); font-weight: 700; font-size: 38px;
    display: flex; align-items: center; justify-content: center;
  }
  .services { position: absolute; left: 48px; top: 388px; margin: 0; padding: 0; list-style: none; }
  .services li { font-size: 29px; color: var(--ink); line-height: 39px; }
  .services .label { position: relative; padding-left: 24px; color: var(--white); text-shadow: 0 1px 2px rgba(0,0,0,0.3); }
  .services .label::before {
    content: ""; position: absolute; left: 2px; top: 14px; width: 12px; height: 12px;
    border-radius: 50%; background: var(--white); box-shadow: 0 1px 2px rgba(0,0,0,0.5);
  }
  .services .detail { display: block; padding-left: 24px; margin-bottom: 2px; }
  .rates { position: absolute; left: 40px; top: 556px; font-family: "Oswald", sans-serif; }
  .rates-main { margin: 0; font-size: 46px; line-height: 56px; color: var(--red); font-weight: 600; }
  .rates-sub { margin: 0; font-size: 37px; line-height: 46px; color: var(--red); font-weight: 500; }
  .rates-example { margin: 4px 0 0; font-size: 21px; color: var(--white); font-weight: 500; }
  .badge { position: absolute; left: 705px; top: 518px; width: 148px; height: 195px; }
  .vehicles {
    position: absolute; left: 40px; top: 735px; width: 850px; height: 255px;
    border-radius: 18px;
    background: linear-gradient(100deg, #e9ecef 0%, #c8ccd0 28%, #e3c33a 55%, #c9302c 62%, #c9a574 75%, #2c3e57 100%);
    opacity: 0.85;
  }
  .notice {
    position: absolute; left: 0; right: 0; margin: 0; text-align: center;
    font-family: "Oswald", sans-serif; font-weight: 400; text-transform: uppercase;
  }
  .notice-insurance { top: 1012px; font-size: 32px; color: var(--red); }
  .notice-lockup { top: 1060px; font-size: 32px; color: var(--green-text); }
  .contact-bar {
    position: absolute; left: 0; right: 0; top: 1117px; height: 50px;
    background: var(--dirt);
    display: flex; align-items: center; justify-content: space-between;
    padding: 0 28px; box-sizing: border-box;
    font-family: "Oswald", sans-serif; font-size: 18px; color: var(--white); text-transform: uppercase;
  }
  .contact-item { display: flex; align-items: center; gap: 7px; white-space: nowrap; }
  .contact-item svg { width: 17px; height: 17px; fill: var(--white); flex: none; }
</style>
</head>
<body>
<main class="flyer">
  <svg class="backdrop" width="907" height="1200" viewBox="0 0 907 1200" aria-hidden="true">
    <defs>
      <linearGradient id="grassFill" x1="0" y1="0" x2="0" y2="1">
        <stop offset="0" stop-color="#8fc640"/>
        <stop offset="1" stop-color="#7cb832"/>
      </linearGradient>
      <linearGradient id="paleFill" x1="0" y1="0" x2="0" y2="1">
        <stop offset="0" stop-color="#ffffff"/>
        <stop offset="1" stop-color="#d9d9d9"/>
      </linearGradient>
    </defs>
    <rect width="907" height="1200" fill="url(#grassFill)"/>
    <path d="M0 780 C 300 760, 650 640, 907 505 L907 1200 L0 1200 Z" fill="var(--dirt)"/>
    <path d="M0 808 C 320 790, 660 680, 907 545 L907 1200 L0 1200 Z" fill="url(#paleFill)"/>
    <rect x="0" y="1167" width="907" height="33" fill="#eeeeee"/>
  </svg>

  <h1 class="business-name">Wattle Downs Truck Parking</h1>

  <h2 class="headline">Ideal for local<br>Redlands Residents</h2>

  <div class="offer-pill">We offer</div>

  <ul class="services">
    <li><span class="label">Parking for:</span>
      <span class="detail">Tipper Trucks &amp; Earthmoving Machinery &amp; Shipping containers</span></li>
    <li><span class="label">Undercover area for:</span>
      <span class="detail">Cars, Motorhomes, Caravans, Horse Floats and Boats</span></li>
  </ul>

  <div class="rates">
    <p class="rates-main">Rates are negotiable</p>
    <p class="rates-sub">on length of time needed</p>
    <p class="rates-example">eg. Truck and Dog = $50 per week + GST</p>
  </div>

  <svg class="badge" viewBox="0 0 148 195" aria-label="20 foot container $25 per week">
    <polygon points="74,2 146,44 146,151 74,193 2,151 2,44" fill="#ffffff"/>
    <polygon points="74,10 139,48 139,147 74,185 9,147 9,48" fill="var(--red)"/>
    <text x="74" y="62" text-anchor="middle" font-family="Oswald, sans-serif" font-size="14" fill="var(--badge-yellow)">20 FOOT CONTAINER</text>
    <text x="74" y="118" text-anchor="middle" font-family="Oswald, sans-serif" font-weight="600" font-size="54" fill="#ffffff">$25</text>
    <text x="74" y="144" text-anchor="middle" font-family="Oswald, sans-serif" font-size="17" fill="var(--badge-yellow)">PER WEEK</text>
  </svg>

  <div class="vehicles" role="img" aria-label="Line-up of vehicles: white motorhome, silver car, yellow tipper truck and a container ship"></div>

  <p class="notice notice-insurance">Owners are responsible for own insurance</p>
  <p class="notice notice-lockup">Lockup parking with owners living on site</p>

  <footer class="contact-bar">
    <span class="contact-item">
      <svg viewBox="0 0 24 24" aria-hidden="true"><path d="M12 2a7 7 0 0 0-7 7c0 5 7 13 7 13s7-8 7-13a7 7 0 0 0-7-7zm0 9.5A2.5 2.5 0 1 1 12 6.5a2.5 2.5 0 0 1 0 5z"/></svg>
      27-31 Banksia Road, Redland Bay QLD 4165
    </span>
    <span class="contact-item">
      <svg viewBox="0 0 24 24" aria-hidden="true"><path d="M6.6 10.8a15 15 0 0 0 6.6 6.6l2.2-2.2a1 1 0 0 1 1-.25 11.4 11.4 0 0 0 3.6.57 1 1 0 0 1 1 1V20a1 1 0 0 1-1 1A17 17 0 0 1 3 4a1 1 0 0 1 1-1h3.5a1 1 0 0 1 1 1c0 1.25.2 2.45.57 3.6a1 1 0 0 1-.25 1z"/></svg>
      Doug Mobile: 0400 118 342
    </span>
    <span class="contact-item">
      <svg viewBox="0 0 24 24" aria-hidden="true"><path d="M6.6 10.8a15 15 0 0 0 6.6 6.6l2.2-2.2a1 1 0 0 1 1-.25 11.4 11.4 0 0 0 3.6.57 1 1 0 0 1 1 1V20a1 1 0 0 1-1 1A17 17 0 0 1 3 4a1 1 0 0 1 1-1h3.5a1 1 0 0 1 1 1c0 1.25.2 2.45.57 3.6a1 1 0 0 1-.25 1z"/></svg>
      Maree Mobile: 0400 562 907
    </span>
  </footer>
</main>
</body>
</html>
```